Flyer Design for an electrical and security company trying to build local customers

I need a flyer design for a new company based in Marlow Shore, Sydney 2299 called "Harbor Quill Dune Electrical and Security" also "HQD Electrical and Security". We are electrical contractors who are looking for more local work including emergency service calls and any project work including renovations or new constructions in the local area. I would like everyone in the area to know I am new and that I am available 24 hours a day 7 days a week. I would like to see designs that use the logo colours. Would also like the font of the entire design to be "juice bold".

Electrical

• juice bold

Requirements
Must have
• Must use the colours of the original logo and also have the information from the rear of the card. Must also have services buttons like the website picture attached.

```html
<!DOCTYPE html>
<html lang="en">
<head>
<meta charset="utf-8">
<title>HQD Electrical and Security – Services Flyer</title>
<link href="https://fonts.googleapis.com/css2?family=Lato:wght@400;700&family=Lora:wght@400;600&display=swap" rel="stylesheet">
<style>
  :root {
    --flyer-bg: #e2c48e;
    --ink: #1c1a17;
    --brand-navy: #1f2d52;
    --brand-blue: #2f6fb3;
    --button-fill: #ecd6ad;
    --canvas-w: 848px;
    --canvas-h: 1200px;
  }
  * { margin: 0; padding: 0; box-sizing: border-box; }
  html, body {
    width: var(--canvas-w);
    height: var(--canvas-h);
    overflow: hidden;
    background: var(--flyer-bg);
  }
  .flyer {
    position: relative;
    width: var(--canvas-w);
    height: var(--canvas-h);
    background: var(--flyer-bg);
    color: var(--ink);
  }
  .flyer__intro {
    position: absolute;
    left: 50px;
    top: 64px;
    width: 752px;
    font-family: "Lato", sans-serif;
    font-size: 20.5px;
    line-height: 26px;
  }
  .service-list {
    position: absolute;
    left: 0;
    top: 195px;
    width: 100%;
    list-style: none;
    text-align: center;
    font-family: "Lora", serif;
    font-size: 23.5px;
  }
  .service-list li {
    height: 45px;
    display: flex;
    justify-content: center;
    align-items: center;
  }
  .service-button {
    display: inline-block;
    height: 38px;
    line-height: 35px;
    padding: 0 22px;
    border: 1.5px solid var(--brand-navy);
    border-radius: 19px;
    background: var(--button-fill);
    color: var(--brand-navy);
  }
  .service-button--urgent {
    background: var(--brand-navy);
    color: var(--flyer-bg);
  }
  .flyer__brand {
    position: absolute;
    left: 0;
    top: 1040px;
    width: 100%;
    display: flex;
    justify-content: center;
    align-items: center;
    gap: 12px;
    font-family: "Lora", serif;
    font-weight: 600;
    font-size: 27px;
    color: var(--brand-navy);
  }
  .flyer__brand-mark {
    width: 16px;
    height: 16px;
    border-radius: 50%;
    background: var(--brand-blue);
  }
  .flyer__location {
    position: absolute;
    left: 0;
    top: 1118px;
    width: 100%;
    text-align: center;
    font-family: "Lato", sans-serif;
    font-size: 21px;
  }
</style>
</head>
<body>
  <main class="flyer">
    <p class="flyer__intro">We are electrical contractors who are looking for more local work including emergency service calls and any project work including renovations or new constructions in the local area. 24*7</p>

    <ul class="service-list">
      <li><span class="service-button service-button--urgent">24 Hours emergency services</span></li>
      <li><span class="service-button">New Installation</span></li>
      <li><span class="service-button">Repair</span></li>
      <li><span class="service-button">Cooktops</span></li>
      <li><span class="service-button">Maintenance</span></li>
      <li><span class="service-button">Renovation/ Extensions</span></li>
      <li><span class="service-button">Stoves</span></li>
      <li><span class="service-button">Security System</span></li>
      <li><span class="service-button">Re-wiring</span></li>
      <li><span class="service-button">Lighting</span></li>
      <li><span class="service-button">Ceiling Fans</span></li>
      <li><span class="service-button">Home Theatre</span></li>
      <li><span class="service-button">Surround Sound</span></li>
      <li><span class="service-button">Telephone</span></li>
      <li><span class="service-button">Wall TVs</span></li>
      <li><span class="service-button">Data</span></li>
      <li><span class="service-button">Electric Hot Water</span></li>
      <li><span class="service-button">Testing and Tagging</span></li>
    </ul>

    <p class="flyer__brand"><span class="flyer__brand-mark"></span>Harbor Quill Dune Electrical and Security</p>

    <p class="flyer__location">Marlow Shore, Sydney 2299</p>
  </main>
</body>
</html>
```